Business Card Design Project

it should have the logo in one side
the other side

Name
Position
telephone
email

Target Market(s)

Business prospects and upscale Fashion shoppers

Industry/Entity Type

Business

Font styles to use
Serif
Sans Serif

Requirements
Must have
• very elegant, upscale, modern
Nice to have
• layering, embossed
Should not have
• Should not use any color OTHER THAN black, silver, white or purple

```html
<!DOCTYPE html>
<html lang="en">
<head>
<meta charset="UTF-8">
<title>Velmora Business Card</title>
<link rel="stylesheet" href="https://fonts.googleapis.com/css2?family=Open+Sans:wght@400;600;700&display=swap">
<style>
  :root {
    --bg: #e6e6e9;
    --card: #ffffff;
    --purple-deep: #2e1740;
    --purple: #5a2d7a;
    --purple-soft: #7a4a9c;
    --silver: #aeb2b8;
    --silver-light: #dcdfe3;
    --black: #161618;
    --ink: #1e1e22;
    --ink-soft: #4a4a50;
    --white: #ffffff;
  }
  * { margin: 0; padding: 0; box-sizing: border-box; }
  html, body {
    width: 1200px; height: 900px; overflow: hidden;
    background: var(--bg);
    font-family: "Open Sans", Arial, sans-serif;
  }
  .canvas {
    width: 1200px; height: 900px;
    display: flex; flex-direction: column; align-items: center; justify-content: center;
    gap: 50px;
  }
  .card {
    position: relative;
    width: 700px; height: 400px;
    background: var(--card);
    border-radius: 46px 6px 46px 6px;
    overflow: hidden;
    box-shadow: 0 10px 28px rgba(0,0,0,0.18);
  }
  .card-wave { position: absolute; inset: 0; width: 100%; height: 100%; }

  .brand {
    display: flex; align-items: center; gap: 12px;
    color: var(--purple);
    font-weight: 600;
    letter-spacing: 4px;
    text-transform: uppercase;
  }
  .brand-mark {
    width: 22px; height: 22px;
    background: var(--silver);
  }

  /* front */
  .front .brand { position: absolute; right: 60px; top: 150px; font-size: 34px; }
  .identity { position: absolute; right: 60px; top: 238px; text-align: right; }
  .identity-name { font-size: 30px; font-weight: 700; color: var(--ink); }
  .identity-role { font-size: 22px; color: var(--ink-soft); margin-top: 2px; }

  .contact {
    position: absolute; left: 34px; top: 225px;
    list-style: none;
    color: var(--white);
    font-size: 15px; line-height: 21px;
  }
  .contact li { display: flex; align-items: flex-start; gap: 8px; }
  .contact .icon { width: 14px; height: 14px; margin-top: 4px; flex-shrink: 0; }
  .contact .address { margin-bottom: 3px; }

  /* back */
  .back .brand {
    position: absolute; left: 50%; top: 50%;
    transform: translate(-50%, -50%);
    font-size: 40px;
  }
</style>
</head>
<body>
<main class="canvas">

  <section class="card front" aria-label="Card front">
    <svg class="card-wave" viewBox="0 0 700 400" preserveAspectRatio="none" aria-hidden="true">
      <defs>
        <linearGradient id="purpleFill" x1="0" y1="0" x2="1" y2="1">
          <stop offset="0" stop-color="#2e1740"/>
          <stop offset="0.6" stop-color="#5a2d7a"/>
          <stop offset="1" stop-color="#7a4a9c"/>
        </linearGradient>
      </defs>
      <path class="wave-band" d="M0 95 C180 85 300 150 380 250 C440 330 520 395 700 395 L700 380 C530 378 460 315 400 235 C315 125 190 75 0 78 Z" fill="var(--black)"/>
      <path class="wave-line" d="M0 135 C180 125 290 175 360 270 C420 350 500 398 640 404" fill="none" stroke="var(--silver)" stroke-width="3"/>
      <path class="wave-fill" d="M0 160 C170 150 270 200 340 290 C390 360 460 400 560 400 L0 400 Z" fill="url(#purpleFill)"/>
    </svg>

    <ul class="contact">
      <li class="address">
        <svg class="icon" viewBox="0 0 14 14"><circle cx="7" cy="7" r="7" fill="#fff"/><path d="M7 3a2.4 2.4 0 0 0-2.4 2.4C4.6 7.2 7 10.5 7 10.5s2.4-3.3 2.4-5.1A2.4 2.4 0 0 0 7 3z" fill="var(--purple)"/></svg>
        <span>Suite # 418, Elm Court,<br>NY 10458</span>
      </li>
      <li>
        <svg class="icon" viewBox="0 0 14 14"><circle cx="7" cy="7" r="7" fill="#fff"/><path d="M4.5 3.5l1.6 1.7-.8 1.1c.5 1 1.3 1.8 2.3 2.3l1.1-.8 1.7 1.6-1 1.1C6.8 10.3 3.7 7.2 3.5 4.5z" fill="var(--purple)"/></svg>
        <span>212-555-0147</span>
      </li>
      <li>
        <svg class="icon" viewBox="0 0 14 14"><circle cx="7" cy="7" r="7" fill="#fff"/><path d="M4.5 3.5l1.6 1.7-.8 1.1c.5 1 1.3 1.8 2.3 2.3l1.1-.8 1.7 1.6-1 1.1C6.8 10.3 3.7 7.2 3.5 4.5z" fill="var(--purple)"/></svg>
        <span>212-555-0183</span>
      </li>
      <li>
        <svg class="icon" viewBox="0 0 14 14"><circle cx="7" cy="7" r="7" fill="#fff"/><rect x="3.5" y="4" width="7" height="6" rx="1" fill="var(--purple)"/></svg>
        <span>212-555-0196</span>
      </li>
      <li>
        <svg class="icon" viewBox="0 0 14 14"><circle cx="7" cy="7" r="7" fill="#fff"/><rect x="3.5" y="4.5" width="7" height="5" fill="var(--purple)"/><path d="M3.5 4.5L7 7.3l3.5-2.8" fill="none" stroke="#fff" stroke-width="0.8"/></svg>
        <span>hello@velmorastudio.com</span>
      </li>
      <li>
        <svg class="icon" viewBox="0 0 14 14"><circle cx="7" cy="7" r="7" fill="#fff"/><circle cx="7" cy="7" r="3.6" fill="none" stroke="var(--purple)" stroke-width="1"/><path d="M3.4 7h7.2M7 3.4v7.2" stroke="var(--purple)" stroke-width="0.8"/></svg>
        <span>www.velmorastudio.com</span>
      </li>
    </ul>

    <div class="brand"><span class="brand-mark"></span><span>Velmora</span></div>

    <div class="identity">
      <p class="identity-name">Adrian Cole</p>
      <p class="identity-role">Owner / C.E.O</p>
    </div>
  </section>

  <section class="card back" aria-label="Card back">
    <div class="brand"><span class="brand-mark"></span><span>Velmora</span></div>
  </section>

</main>
</body>
</html>
```